Tellwick Asset Management - Corporate Letter Head Project

Looking for a classy design based on our current logo. Please find current logo source file in files. With our color scheme.

Target Market(s)

We're an investment firm, the letterhead needs to look professional and attractive to clients.

Industry/Entity Type

Hedgefund

Colors
0054AA
0677BA
7BADD7
CADEEF
E8F1F8

Requirements
Must have
• Our logo, address, phone number, and email

```html
<!DOCTYPE html>
<html lang="en">
<head>
<meta charset="utf-8">
<title>Tellwick Asset Management – Letterhead</title>
<link href="https://fonts.googleapis.com/css2?family=Cormorant+Garamond:wght@500&family=Open+Sans:wght@400&display=swap" rel="stylesheet">
<style>
  :root {
    --navy: #1f2a4a;
    --paper: #ffffff;
    --backdrop: #c9c9c9;
    --ink-light: #ffffff;
  }
  * { margin: 0; padding: 0; box-sizing: border-box; }
  html, body {
    width: 1200px; height: 686px; overflow: hidden;
    background: var(--backdrop);
  }
  .letterhead {
    position: absolute;
    left: 370px; top: 18px;
    width: 460px; height: 650px;
    background: var(--paper);
    box-shadow: 0 6px 22px rgba(0,0,0,0.25);
    overflow: hidden;
  }
  .header-band {
    position: absolute; left: 0; top: 0;
    width: 100%; height: 80px;
    background: var(--navy);
    display: flex; align-items: center;
    padding: 0 22px;
    color: var(--ink-light);
  }
  .brand { display: flex; align-items: center; gap: 12px; }
  .brand-square {
    width: 34px; height: 34px;
    border: 1px solid var(--ink-light);
  }
  .brand-name {
    font-family: "Cormorant Garamond", serif;
    font-weight: 500;
    color: var(--ink-light);
    line-height: 1;
  }
  .brand-name .primary { display: block; font-size: 21px; letter-spacing: 0.5px; }
  .brand-name .secondary { display: block; font-size: 9.5px; letter-spacing: 5.2px; margin-top: 4px; }
  .divider {
    width: 1px; height: 48px;
    background: var(--ink-light);
    margin: 0 16px 0 auto;
  }
  .contact {
    font-family: "Open Sans", sans-serif;
    font-size: 8.5px; line-height: 1.35;
    list-style: none;
  }
  .contact li { display: flex; align-items: flex-start; gap: 6px; }
  .contact svg { width: 8px; height: 8px; margin-top: 2px; flex: none; }
  .footer-wave {
    position: absolute; left: 0; bottom: 0;
    width: 460px; height: 240px;
  }
</style>
</head>
<body>
  <main class="letterhead">
    <header class="header-band">
      <div class="brand">
        <span class="brand-square"></span>
        <span class="brand-name">
          <span class="primary">TELLWICK ASSET</span>
          <span class="secondary">MANAGEMENT</span>
        </span>
      </div>
      <span class="divider"></span>
      <ul class="contact">
        <li>
          <svg viewBox="0 0 10 10"><path d="M5 0.5a3.2 3.2 0 0 0-3.2 3.2C1.8 6 5 9.5 5 9.5S8.2 6 8.2 3.7A3.2 3.2 0 0 0 5 0.5zm0 4.5a1.3 1.3 0 1 1 0-2.6 1.3 1.3 0 0 1 0 2.6z" fill="#fff"/></svg>
          <span>27 Harrow Lane<br>Fenbridge, Kent, FN4 7QT</span>
        </li>
        <li>
          <svg viewBox="0 0 10 10"><path d="M2.2 0.8l1.6 0 .6 2.2-1 .8a5.5 5.5 0 0 0 2.8 2.8l.8-1 2.2.6 0 1.6c0 .6-.5 1.2-1.2 1.2A8 8 0 0 1 1 2c0-.7.5-1.2 1.2-1.2z" fill="#fff"/></svg>
          <span>(555) 204-6173</span>
        </li>
        <li>
          <svg viewBox="0 0 10 10"><circle cx="5" cy="5" r="4.2" fill="none" stroke="#fff" stroke-width="1"/><path d="M0.8 5h8.4M5 0.8c-2 2.4-2 6 0 8.4M5 0.8c2 2.4 2 6 0 8.4" fill="none" stroke="#fff" stroke-width="0.8"/></svg>
          <span>www.tellwickam.com</span>
        </li>
        <li>
          <svg viewBox="0 0 10 10"><rect x="0.8" y="2" width="8.4" height="6" fill="none" stroke="#fff" stroke-width="1"/><path d="M0.8 2l4.2 3.4L9.2 2" fill="none" stroke="#fff" stroke-width="1"/></svg>
          <span>office@tellwickam.com</span>
        </li>
      </ul>
    </header>

    <svg class="footer-wave" viewBox="0 0 460 240" aria-hidden="true">
      <path d="M150 240 C270 225 320 150 360 95 C395 48 425 25 460 15 L460 240 Z" fill="var(--navy)"/>
      <path d="M165 226 C275 205 315 135 355 82 C390 36 425 14 460 6" fill="none" stroke="var(--paper)" stroke-width="6"/>
      <path d="M170 221 C275 198 312 128 352 76 C388 30 425 8 460 0" fill="none" stroke="var(--navy)" stroke-width="3"/>
    </svg>
  </main>
</body>
</html>
```